body therapist

I need to offer my services as a massage therapist at home, acclimating customer space aroma candles with music and everything else to bring comfort. 8 offer rituals like this: relaxing ritual, purifying ritual, ritual breast, facial and body cleansing ritual organic, ritual man, ritual feet, slimming ritual. Naraja handling colors, seawater, green, lavender

Target Market(s)

men and women, tired, stressed, looking for something new

Font styles to use
Decorative
Script

Colors
f37122
0493ce
abd037

Requirements
Must have
• detailing each massage
Nice to have
• simple and elegant

```html
<!DOCTYPE html>
<html lang="es">
<head>
<meta charset="utf-8">
<title>Rituales de masaje a domicilio</title>
<link href="https://fonts.googleapis.com/css2?family=Pinyon+Script&family=Crimson+Text:ital,wght@0,400;0,600;1,400&family=Lora:ital,wght@0,600;0,700;1,400;1,600;1,700&display=swap" rel="stylesheet">
<style>
  :root{
    --paper:#ffffff;
    --ink:#2a2220;
    --muted:#5a4a45;
    --panel:#ede1dd;
    --band:#c8b0a8;
    --orange:#f37122;
    --blue:#0493ce;
    --green:#abd037;
    --lavender:#a88bc7;
    --photo-skin:#c98a5c;
    --photo-warm:#e9d6c0;
    --photo-rose:#d99a8a;
  }
  *{margin:0;padding:0;box-sizing:border-box}
  html,body{width:1200px;height:928px;overflow:hidden;background:var(--paper)}
  .brochure{position:relative;width:1200px;height:928px;color:var(--ink);font-family:"Crimson Text",Georgia,serif}
  .abs{position:absolute}

  .title{left:50px;top:40px;font-family:"Pinyon Script",cursive;font-weight:400;font-size:30px;color:#3a3030;white-space:nowrap}
  .title .num{font-size:42px;color:var(--orange)}
  .body-text{font-size:16px;line-height:16.8px;text-align:justify;hyphens:auto}
  .intro{left:52px;top:100px;width:496px}
  .intro p{margin-bottom:16px;text-align:left}
  .dropcap{float:left;font-size:54px;line-height:40px;font-weight:600;margin:4px 6px 0 0}
  .col{width:237px}
  .col p{margin-bottom:17px}

  .services-panel{left:600px;top:80px;width:600px;height:300px;background:var(--panel);border-top:7px solid var(--band)}
  .logo-mark{left:836px;top:28px;width:140px;height:84px;border-radius:50%;background:radial-gradient(ellipse at center,#e4d8d4 0%,#f6f0ee 60%,rgba(255,255,255,0) 72%)}
  .services-title{left:636px;top:110px;font-family:"Lora",serif;font-style:italic;font-weight:700;font-size:19px}
  .services{left:636px;top:140px;width:295px;list-style:none}
  .services li{margin-bottom:3px}
  .ritual{display:block;font-family:"Lora",serif;font-weight:700;font-size:15.5px;line-height:17px}
  .ritual .n{color:var(--orange)}
  .detail{display:block;font-style:italic;font-size:12px;line-height:13px;color:var(--muted)}
  .colors{left:944px;top:212px;list-style:none;font-family:"Lora",serif;font-weight:700;font-size:17px;line-height:26px}
  .colors li{display:flex;align-items:center;gap:8px}
  .dot{width:12px;height:12px;border-radius:50%}

  .rule-left{left:0;top:377px;width:600px;height:6px;background:var(--band)}
  .photo{top:384px;height:290px}
  .photo-back{left:0;width:274px;background:linear-gradient(90deg,var(--photo-skin),#b87a52 60%,#e6d3b8)}
  .photo-couple{left:276px;width:502px;background:linear-gradient(120deg,#ebe2d3,var(--photo-warm) 45%,#f4ead8)}
  .photo-petals{left:780px;width:420px;background:linear-gradient(110deg,#a86a45,var(--photo-skin) 50%,var(--photo-rose))}

  .contact-band{left:600px;top:676px;width:600px;height:60px;background:var(--panel);border-bottom:5px solid var(--band);display:flex;align-items:center;justify-content:center;font-family:"Lora",serif;font-style:italic;font-weight:600;font-size:20.5px}
  .tagline{left:612px;top:766px;width:270px;text-align:center;font-family:"Lora",serif;font-style:italic;font-weight:600;font-size:20px;line-height:25.6px}
  .phone{left:920px;top:762px;font-family:"Lora",serif;font-style:italic;font-weight:600;font-size:31px;white-space:nowrap;display:flex;align-items:center;gap:8px}
  .hours{left:920px;top:815px;width:240px;text-align:center;font-family:"Lora",serif;font-style:italic;font-weight:600;font-size:19.5px;line-height:25.6px}
</style>
</head>
<body>
<div class="brochure">
  <h1 class="abs title">Estos son los <span class="num">6</span> beneficios de un masaje relajante</h1>

  <div class="abs intro body-text">
    <p><span class="dropcap">E</span>l estrés de nuestro día a día puede afectarte, y mucho, tanto física como psicológicamente.</p>
    <p>Lo que te proponemos no es la solución definitiva, pero sí puede ayudarte a recuperar fuerzas para afrontar tu rutina diaria.</p>
    <p style="margin-bottom:2px">Y es que un masaje relajante tienes más beneficios para nuestra salud de los que pensábamos:</p>
  </div>

  <div class="abs col body-text" style="left:54px;top:245px">
    <p>1. Con un masaje relajante, conseguimos terminar con problemas musculares como las contracturas, provocados por una mala postura prolongada, un movimiento brusco o incluso por el estrés.</p>
  </div>
  <div class="abs col body-text" style="left:311px;top:245px">
    <p>2. Un masaje relajante mejora la circulación sanguínea en todo el cuerpo y, como consecuencia, se produce un aumento del aporte de oxígeno en los tejidos y los órganos, beneficiando nuestra salud en general.</p>
  </div>

  <div class="abs services-panel"></div>
  <div class="abs logo-mark" role="img" aria-label="Ilustración de una persona recibiendo un masaje"></div>
  <h2 class="abs services-title">8 Servicios de Relajamiento</h2>
  <ul class="abs services">
    <li><span class="ritual"><span class="n">1.</span> Ritual Relajante</span><span class="detail">Aceites tibios, velas aromáticas y música suave.</span></li>
    <li><span class="ritual"><span class="n">2.</span> Ritual Purificante</span><span class="detail">Exfoliación y presión profunda que liberan toxinas.</span></li>
    <li><span class="ritual"><span class="n">3.</span> Ritual Mama</span><span class="detail">Masaje delicado y seguro para futuras mamás.</span></li>
    <li><span class="ritual"><span class="n">4.</span> Ritual Limpieza Organica<br>&nbsp;&nbsp;&nbsp;&nbsp;Facial y Corporal</span><span class="detail">Limpieza de rostro y cuerpo con productos orgánicos.</span></li>
    <li><span class="ritual"><span class="n">5.</span> Ritual Hombre</span><span class="detail">Presión firme en espalda, cuello y hombros.</span></li>
    <li><span class="ritual"><span class="n">5.</span> Rrtual Pies</span><span class="detail">Reflexología y aromas para piernas cansadas.</span></li>
    <li><span class="ritual"><span class="n">6.</span> Ritual Adelgazante.</span><span class="detail">Masaje reductor que activa la circulación.</span></li>
  </ul>
  <ul class="abs colors">
    <li>Manejando colores</li>
    <li><span class="dot" style="background:var(--orange)"></span>1. Naraja</li>
    <li><span class="dot" style="background:var(--blue)"></span>1. Agua Marina</li>
    <li><span class="dot" style="background:var(--green)"></span>1. Verde</li>
    <li><span class="dot" style="background:var(--lavender)"></span>1. Lavanda</li>
  </ul>

  <div class="abs rule-left"></div>
  <div class="abs photo photo-back" role="img" aria-label="Fotografía de manos masajeando una espalda junto a orquídeas y velas"></div>
  <div class="abs photo photo-couple" role="img" aria-label="Fotografía de una pareja en camillas de masaje con velas encendidas"></div>
  <div class="abs photo photo-petals" role="img" aria-label="Fotografía de una mujer recibiendo masaje rodeada de pétalos de rosa"></div>

  <div class="abs col body-text" style="left:54px;top:692px">
    <p>3. Aumenta el flujo del líquido linfático mejorando nuestro sistema linfático, el encargado que terminar con las toxinas y otros contaminantes de nuestro cuerpo.</p>
    <p>4. Al eliminar las toxinas del cuerpo y las células muertas, el masaje corporal nos ayuda a tener una piel más sana y hermosa.</p>
  </div>
  <div class="abs col body-text" style="left:311px;top:692px">
    <p>5. Promueve la respiración profunda y lenta lo que nos beneficia en cuerpo y mente. No sólo aumenta el nivel del oxígeno en nuestro cuerpo sino que además nos reja y aplaca la ansiedad.</p>
    <p>6. Al proporcionarnos esa sensación de relax, este tipo de masajes nos ayudan a disipar las tensiones y las preocupaciones del día a día.</p>
  </div>

  <div class="abs contact-band">Contactanos para hacer una cita a domicilio</div>
  <p class="abs tagline">Nos esforzamos por ofrecer la mejor experiencia profecional de masaje que sea posible.</p>
  <div class="abs phone">
    <svg width="22" height="26" viewBox="0 0 24 28" aria-hidden="true"><path fill="#2a2220" d="M6 1c1.5-.6 2.6.2 3.2 1.4l2 4.3c.5 1.1.2 2.2-.8 2.9l-1.8 1.3c1 3.3 3 6.2 5.6 8.2l1.9-1.1c1-.6 2.2-.4 2.9.5l2.8 3.8c.8 1.1.5 2.5-.7 3.2l-1.8 1.1C14.8 28.6 2.3 17.2 2.9 4.4 3 3 4 1.8 6 1z"/></svg>
    1 800-555-0142
  </div>
  <p class="abs hours">Lunes a Sabado<br>8 a 21 hrs.</p>
</div>
</body>
</html>
```